Creative Stationary for Solo Law Firm

I am looking for stationary designs for my solo law firm called TM Halvorsen Law PLLC. My logo is attached. I'd like the logo incorporated into the design.

I'm looking for a stationary design that is a bit outside of the box and not too standard or boring. The final design should communicate professionalism.

Target Market(s)

United States Clients, Opposing Counsel

Industry/Entity Type

Legal

Font styles to use
Sans Serif

Requirements
Must have
• The stationary design must incorporate my logo design attached. The design itself must be creative. The envelope design must follow standard United States designs with room for the postage stamp at the top right corner and space for the recipient's address in the middle.

```html
<!DOCTYPE html>
<html lang="en">
<head>
<meta charset="utf-8">
<title>TM Halvorsen Law PLLC – Stationery</title>
<link rel="stylesheet" href="https://fonts.googleapis.com/css2?family=Cinzel:wght@400&family=Open+Sans:ital,wght@0,400;0,700;1,400&display=swap">
<style>
  :root{
    --navy:#022360;
    --slate:#555555;
    --backdrop:#999999;
    --paper:#ffffff;
    --ink:#1a1a1a;
    --muted:#444444;
  }
  *{margin:0;padding:0;box-sizing:border-box}
  html,body{width:1200px;height:1200px;overflow:hidden;background:var(--backdrop)}
  body{position:relative;font-family:"Open Sans",Arial,sans-serif;color:var(--ink)}
  .sheet{position:absolute;background:var(--paper);overflow:hidden}
  .wordmark{font-family:"Cinzel",Georgia,serif;font-weight:400;color:var(--navy);white-space:nowrap;letter-spacing:0.01em;position:absolute}
  .wordmark.light{color:var(--paper)}
  .band{position:absolute;left:0;bottom:0;width:100%}
  .contact{position:absolute;font-size:6.5px;line-height:8.2px;color:var(--muted)}
  .contact b{color:var(--navy);font-weight:700}
  .web{position:absolute;color:#fff;font-style:italic;font-size:8.5px;letter-spacing:0.55em}

  /* brand panel */
  .brand-panel{left:80px;top:28px;width:1040px;height:416px}
  .brand-panel .wordmark{left:0;width:100%;text-align:center;top:186px;font-size:78px;line-height:1}

  /* business card */
  .card-front{left:80px;top:476px;width:250px;height:152px}
  .card-front .wordmark{left:38px;top:35px;font-size:20px}
  .card-person{position:absolute;right:125px;top:95px;text-align:right;font-size:6px;line-height:7px;color:var(--muted)}
  .card-person .name{font-size:10.5px;line-height:12px;color:var(--navy)}
  .card-divider{position:absolute;left:126px;top:94px;width:1px;height:34px;background:#bbb}
  .card-front .contact{left:131px;top:96px;line-height:7.6px;font-size:5.5px}
  .card-back{left:342px;top:476px;width:250px;height:152px;background:var(--navy)}
  .card-back .wordmark{left:0;width:100%;text-align:center;top:62px;font-size:20px}

  /* #10 envelope front */
  .envelope-front{left:80px;top:678px;width:512px;height:221px}
  .envelope-front .wordmark{left:23px;top:25px;font-size:19px}
  .envelope-front .contact{left:398px;top:15px}
  .envelope-front .web{left:327px;bottom:6px}

  /* envelope back */
  .envelope-back{left:80px;top:952px;width:512px;height:221px}
  .envelope-back svg{position:absolute;left:0;top:0}
  .envelope-back .wordmark{left:0;width:100%;text-align:center;top:28px;font-size:21px}

  /* letterhead */
  .letterhead{left:627px;top:476px;width:493px;height:697px}
  .letterhead .wordmark{left:27px;top:29px;font-size:24px}
  .letterhead .contact{left:385px;top:14px}
  .letter-body{position:absolute;left:45px;top:150px;width:403px;font-size:10.5px;line-height:14px}
  .letter-body p{margin-bottom:15px}
  .letter-body .prose{text-align:justify;line-height:19.2px;margin-bottom:4px}
  .letter-body .close{margin-top:14px}
  .letter-body .sign{font-weight:700;margin-top:16px}
  .letterhead .web{left:314px;bottom:5px}
</style>
</head>
<body>

<section class="sheet brand-panel">
  <div class="wordmark">TM HALVORSEN LAW</div>
</section>

<section class="sheet card-front">
  <div class="wordmark">TM HALVORSEN LAW</div>
  <div class="card-person">
    <div class="name">Your Name</div>
    <div>Manager</div>
    <div style="margin-top:3px">0000 Grand Point</div>
    <div>USA</div>
  </div>
  <div class="card-divider"></div>
  <div class="contact">
    <div><b>P</b> : 0123-456-789</div>
    <div><b>C</b> : 0123-456-789</div>
    <div><b>F</b> : 0123-456-789</div>
    <div><b>E</b> : office@tmhlaw.com</div>
  </div>
  <svg class="band" width="250" height="15" viewBox="0 0 250 15">
    <polygon points="0,5 140,5 133,15 0,15" fill="var(--navy)"/>
    <polygon points="148,0 250,0 250,15 136,15" fill="var(--slate)"/>
  </svg>
</section>

<section class="sheet card-back">
  <div class="wordmark light">TM HALVORSEN LAW</div>
</section>

<section class="sheet envelope-front">
  <div class="wordmark">TM HALVORSEN LAW</div>
  <div class="contact">
    <div>45 Birchwood Ln Austin, TX 78701</div>
    <div><b>P</b> : 0123-456-789</div>
    <div><b>C</b> : 0123-456-789</div>
    <div><b>F</b> : 0123-456-789</div>
    <div><b>E</b> : office@tmhlaw.com</div>
  </div>
  <svg class="band" width="512" height="23" viewBox="0 0 512 23">
    <polygon points="0,6 291,6 279,23 0,23" fill="var(--navy)"/>
    <polygon points="302,0 512,0 512,23 284,23" fill="var(--slate)"/>
  </svg>
  <div class="web">www.tmhlaw.com</div>
</section>

<section class="sheet envelope-back">
  <svg width="512" height="90" viewBox="0 0 512 90">
    <path d="M0,0 H512 L502,32 Q496,50 470,53 Q380,62 300,74 Q256,80 212,74 Q130,62 42,53 Q16,50 10,32 Z" fill="var(--navy)"/>
  </svg>
  <div class="wordmark light">TM HALVORSEN LAW</div>
</section>

<section class="sheet letterhead">
  <div class="wordmark">TM HALVORSEN LAW</div>
  <div class="contact">
    <div>45 Birchwood Ln Austin, TX 78701</div>
    <div><b>P</b> : 0123-456-789</div>
    <div><b>C</b> : 0123-456-789</div>
    <div><b>F</b> : 0123-456-789</div>
    <div><b>E</b> : office@tmhlaw.com</div>
  </div>
  <div class="letter-body">
    <p>Date</p>
    <p>Recipient Name</p>
    <p>Company Name<br>Street Address<br>City, State, Zip</p>
    <p class="prose">This is the template of the letterhead of the official Example club. The typeface used is Arial 10.5 pt with 12.5 pt line spacing. This text is so-called dummy text and has no meaning. This dummy text is not meant to be read. Its only purpose is to demonstrate the size, colour and position of the text within the correct format. The typeface used is Arial 10.5 pt with 12.5 pt line spacing. This text is so-called dummy text and has no meaning. This dummy text is not meant to be read. Its only purpose is to demonstrate the size, colour and position of the text within the correct format. The typeface usedis Arial 10.5 pt with 12.5 pt line spacing. This text is so-called dummy text and has no meaning</p>
    <p class="prose" style="text-align:left">It only purpose is to demonstrate the size, colour and position of the text within the correct format.</p>
    <p class="close">Yours Sincerely,</p>
    <p class="sign">Sample</p>
  </div>
  <svg class="band" width="493" height="23" viewBox="0 0 493 23">
    <polygon points="0,5 277,5 265,23 0,23" fill="var(--navy)"/>
    <polygon points="287,0 493,0 493,23 270,23" fill="var(--slate)"/>
  </svg>
  <div class="web">www.tmhlaw.com</div>
</section>

</body>
</html>
```